Brocure for Brindlo - Social Media Management

Brindlo is a Dutch company in the market of Social Media growth. We need a brochure (digital/PDF) for our company. Please see attached word doc for the text and attached logo. The initial proposal can contain just the first 4 pages text of the word doc.

We use informal language in all our communication.

Slogan: Effectieve Social Media Marketing voor professionals en ondernemers

Website: brindlopq.nl

Industry/Entity Type

Digital Marketing

Contact Information for Business Card

Contact details:

Joris ter Haaksel
joris@brindlopq.nl
06-47915328

```html
<!DOCTYPE html>
<html lang="nl">
<head>
<meta charset="utf-8">
<title>Brindlo – brochure social media marketing</title>
<link href="https://fonts.googleapis.com/css2?family=Roboto:ital,wght@0,400;0,500;0,700;0,900;1,700&display=swap" rel="stylesheet">
<style>
:root{
  --navy:#15264a;
  --navy-deep:#0d1a35;
  --navy-soft:#2a3d66;
  --orange:#ec7422;
  --paper:#ffffff;
  --ink:#414a5a;
  --muted:#7d8594;
  --backdrop:#e7e9ed;
  --table-head:#4d82c4;
  --table-group:#dfe8f5;
  --tick:#3aa346;
}
*{box-sizing:border-box;margin:0;padding:0}
html,body{width:1200px;height:1000px;overflow:hidden}
body{position:relative;background:var(--backdrop);font-family:"Roboto",Arial,sans-serif;color:var(--ink)}
.backdrop{position:absolute;inset:0}
.page{position:absolute;background:var(--paper);overflow:hidden;font-size:4.3px;line-height:1.45;box-shadow:0 2px 6px rgba(0,0,0,.25)}
.page p{margin:0 0 3.5px}
.pad{padding:10px 12px}
.page h2{font-size:9px;font-weight:700;color:var(--navy);margin:6px 0 4px;line-height:1.15}
.page .on-dark h2,.on-dark h2{color:#fff}
.on-dark{color:#dfe4ee}
.label{display:inline-block;background:var(--navy);color:#fff;font-size:4.5px;font-weight:700;padding:2px 5px;margin-bottom:5px}
.sub{font-size:5.8px;font-style:italic;font-weight:700;color:var(--navy);border-bottom:.6px solid #b9c0cc;padding:0 0 2px 0;margin:6px 0 4px;display:flex;align-items:center;gap:4px}
.sub::before{content:"";width:3px;height:3px;border-radius:50%;background:var(--navy)}
.on-dark .sub{color:#fff;border-color:#5a6b8e}
.on-dark .sub::before{background:#fff}
.sub.accent::before{background:var(--orange)}
.list{list-style:none;margin:0 0 4px}
.list li::before{content:"• "}
.mono-list{font-family:"Roboto Mono","Courier New",monospace;list-style:none;font-size:4.6px}
.mono-list li::before{content:"• "}
.page-foot{position:absolute;left:0;right:0;bottom:0;height:28px;padding:0 12px;display:flex;align-items:center;justify-content:space-between}
.foot-url{font-size:4.6px;letter-spacing:.6px;color:var(--ink);border-top:.6px solid #c7ccd5;padding-top:3px;width:58%}
.brand-tag{display:flex;align-items:center;gap:3px;font-size:6.5px;font-weight:700;color:var(--navy)}
.brand-tag::before{content:"";width:7px;height:7px;border-radius:50%;border:1px solid currentColor}
.page-foot.dark{background:var(--navy)}
.page-foot.dark .foot-url{color:#fff;border-color:#5a6b8e}
.page-foot.dark .brand-tag{color:#fff}
.navy-fill{background:var(--navy)}
.photo{position:absolute}
/* cover */
.cover{background:var(--navy-deep)}
.cover .photo{inset:0;background:linear-gradient(160deg,#223559 0%,#142444 45%,#0b1630 100%)}
.cover-brand{position:absolute;left:12px;top:12px;width:58px;height:44px;background:#fff;display:flex;align-items:center;justify-content:center}
.cover-brand .brand-tag{font-size:9px}
.cover-brand .brand-tag::before{width:9px;height:9px}
.cover-title{position:absolute;left:12px;top:86px;line-height:1.05}
.cover-title .t-lead{font-size:13px;font-weight:700;color:#fff}
.cover-title .t-small{font-size:6.4px;color:#fff;display:block;margin:1px 0}
.cover-title .t-small.orange{color:var(--orange)}
.cover-title .t-big{font-size:17.5px;font-weight:700;color:var(--orange);display:block}
.cover-url{position:absolute;left:12px;bottom:14px;width:160px;font-size:4.8px;color:#fff;letter-spacing:.7px;border-top:.6px solid #56688c;padding-top:3px}
/* table */
.services{width:100%;border-collapse:collapse;font-size:3.4px;margin-top:4px}
.services th{background:var(--table-head);color:#fff;font-weight:500;padding:1.5px 1px;text-align:center;line-height:1.1}
.services th:first-child{text-align:left}
.services td{border-bottom:.4px solid #d6dbe3;padding:.8px 1px;text-align:center;color:var(--tick);font-size:4.2px;line-height:1.1}
.services td:first-child{text-align:left;color:var(--ink);font-size:3.4px;white-space:nowrap}
.services tr.group td{background:var(--table-group);color:var(--navy);font-weight:700}
.big-brand{position:absolute;left:940px;top:758px;width:236px;text-align:center}
.big-brand .ring{width:76px;height:76px;border-radius:50%;border:5px solid var(--navy);margin:0 auto 10px}
.big-brand .name{font-size:58px;font-weight:700;color:var(--navy);letter-spacing:2px;line-height:1}
</style>
</head>
<body>

<svg class="backdrop" width="1200" height="1000" viewBox="0 0 1200 1000" aria-hidden="true">
  <rect width="1200" height="1000" fill="#e7e9ed"/>
  <polygon points="0,0 1150,0 0,800" fill="#15264a"/>
</svg>

<!-- Row 1 -->
<section class="page cover" style="left:41px;top:75px;width:198px;height:248px">
  <div class="photo" role="img" aria-label="Donkerblauwe sfeerfoto van een werkplek als achtergrond"></div>
  <div class="cover-brand"><span class="brand-tag">Brindlo</span></div>
  <div class="cover-title">
    <span class="t-lead">Effectieve</span>
    <span class="t-small">social media marketing</span>
    <span class="t-small orange">voor</span>
    <span class="t-big">professionals</span>
    <span class="t-small">en</span>
    <span class="t-big">ondernemers</span>
  </div>
  <div class="cover-url">brindlopq.nl</div>
</section>

<section class="page navy-fill" style="left:255px;top:75px;width:197px;height:248px">
  <div class="pad" style="background:#fff;padding-bottom:6px">
    <span class="label">Groei, interactie en content</span>
    <p>Je bereik vergroten, traffic genereren en daarmee meer omzet behalen. Dat is wat wij bieden.</p>
    <p>Onze services helpen jouw bereik op de sociale media te vergroten. Met een uitgekiende groeistrategie, onze kennis en geavanceerde tools zorgen we voor gerichte content en interactie op je sociale netwerken. (actieve interactie + relevante content) = actieve volgers = (+ traffic + omzet)</p>
  </div>
  <div class="pad on-dark">
    <h2>Wie zijn wij?</h2>
    <p>Wij zijn Brindlo. Een team van social media experts dat je sociale netwerk activeert en het bereik vergroot. We zorgen voor sociale interactie met volgers, nieuwe en bestaande. Daarmee genereren we traffic naar je website/shop.</p>
    <p>Het doel? Meer omzet. Simpel en heel meetbaar.</p>
    <h2>Voor wie?</h2>
    <p>Onze dienstverlening kan ingezet worden op zowel persoonlijke zakelijke profielen (bv Vaklink) of voor bedrijfspagina's op diverse sociale mediakanalen.</p>
  </div>
  <div class="page-foot" style="background:#fff"><span class="foot-url">brindlopq.nl</span><span class="brand-tag">Brindlo</span></div>
</section>

<section class="page" style="left:468px;top:75px;width:217px;height:248px;background:var(--navy)">
  <div class="pad" style="background:#fff;height:158px">
    <span class="label">Groei, interactie en content</span>
    <h2>Wat doen we?</h2>
    <p>Samen met jou bepalen we je doelen in de sociale netwerken. Zowel strategisch als tactisch en operationeel. Wij richten ons op die doelen en zorgen voor een netwerk van echte en actieve volgers. Of het nu gaat om Vaklink, Beeldstip, Vriendhub of Piepnet, interactie zorgt voor betrokken volgers. Die is vervolgens in je verkoopproces kunt oppakken.</p>
    <p>Voor <b>zakelijke professionals</b> verzorgen wij personal branding met als doel impact en sociaal sales. We zorgen voor veel meer relevante connecties en activeren je zakelijke netwerk. Gecombineerd met de juiste contentstrategie, zorgen wij ervoor dat je gezien wordt als autoriteit in je vakgebied.</p>
    <p>Onze diensten voor <b>bedrijven</b> bestaan uit de verschillende organische groei van het volgernetwerk, het activeren van het netwerk met content en interactie. We zorgen daarmee voor een groot bereik en verkeer naar je website.</p>
  </div>
  <div class="pad" style="background:#fff;position:absolute;left:0;right:0;top:166px;bottom:0">
    <h2 style="margin-top:0">Welke platformen?</h2>
    <p>We bieden onze diensten aan op alle belangrijke platformen:</p>
    <ul class="list">
      <li>Vaklink (bedrijfspagina's en persoonlijke profielen)</li>
      <li>Vriendhub (bedrijfspagina's en groepen)</li>
      <li>Beeldstip (bedrijfspagina's en persoonlijke profielen)</li>
    </ul>
  </div>
  <div class="page-foot" style="background:#fff"><span class="foot-url">brindlopq.nl</span><span class="brand-tag">Brindlo</span></div>
</section>

<section class="page navy-fill" style="left:712px;top:60px;width:205px;height:265px">
  <div class="pad" style="background:#fff;height:183px">
    <ul class="mono-list">
      <li>Piepnet</li><li>Vidzaal</li><li>Zoekly Bedrijf</li><li>Optioneel: Klipklap, Prikwand, Draadnet en Tuimel</li>
    </ul>
    <h2>Waarom kies je voor ons?</h2>
    <p>Jij hebt jouw vak, wij het onze. Als iedereen doet waar hij goed in is, worden daar allemaal beter van. Wij zijn goed in het activeren en vergroten van je sociale netwerk. Daarvoor gebruiken we een slimme mix van kennis en tools.</p>
    <p>Een strategie die ervoor zorgt dat je kunt focussen op je corebusiness. Met onze slimme tools vergroten wij de impact van je sociale netwerken. Met als resultaat: meer traffic, meer leads, meer omzet.</p>
    <h2>Doen we alles zelf?</h2>
    <p>Wij zijn slim in de strategie en systemen voor het vergroten van interactie. En we hebben een netwerk van specialisten die slim zijn in hun vak. Zoals een reclamebureau, creatief ontwerper, websitebouwer of marketingstrategiebureau.</p>
    <p>Is er op dat vlak een behoefte, dan brengen wij je graag in contact.</p>
  </div>
  <div class="pad on-dark">
    <h2 style="margin-top:2px">Hoe lang gaan we met elkaar in zee?</h2>
    <p>Een groeistrategie werkt op de lange termijn het beste als die groei organisch is. En dat vraagt dus ook een strategie voor de lange termijn. Lang is relatief, maar je moet erop rekenen dat we minimaal een jaar nodig hebben om de groeistrategie optimaal te laten werken.</p>
  </div>
  <div class="page-foot dark"><span class="foot-url">brindlopq.nl</span><span class="brand-tag">Brindlo</span></div>
</section>

<section class="page navy-fill" style="left:957px;top:60px;width:201px;height:265px">
  <div class="pad on-dark">
    <p>Natuurlijk is er in elke situatie snelle winst te behalen. Maar voor een goede samenwerking is het belangrijk dat je elkaar leert kennen en begrijpen. Daarom vragen we ook regelmatig jouw energie en input.</p>
    <h2 style="margin-top:10px">Groeien op sociale media</h2>
    <p>Het staat als een paal boven water: sociale media zijn een krachtig marketinginstrument. Een kans die je niet voorbij kunt laten gaan, of je dat nou leuk vindt of niet. Het geeft je de kans om je merk op te bouwen, je zicht- en vindbaarheid te verbeteren en uiteindelijk meer leads en verkopen te genereren.</p>
    <p>Het beheren van je sociale platforms is een tijdrovende klus. En om resultaat te krijgen, moet je het ook nog eens slim doen. Om de online herkenbaarheid van je bedrijf te vergroten, zijn je uitingen de sleutel.</p>
    <p>Interactie, consistentie, responsiveness, allemaal zorgen ze voor herkenning en betrokkenheid van je volgers. We helpen je om je digitale activiteiten met elkaar te verbinden en je bedrijf te laten groeien.</p>
    <div class="sub">Volledig social management</div>
    <p>We bieden een compleet beheerpakket voor sociale media waarmee we betrokkenheid van volgers realiseren en tijdig en altijd proactief schakelen met de volgende stap. Zo blijven bezoekers geboeid en actief.</p>
    <p>We plannen zowel doelgroep- als branche specifieke inhoud en combineren online aanwezigheid om meer en meer gericht.</p>
  </div>
</section>

<!-- Row 2 -->
<section class="page" style="left:41px;top:377px;width:198px;height:256px">
  <div class="pad">
    <div class="sub" style="margin-top:0">Activeren van je netwerk</div>
    <p>Je bent al een poos bezig met het beheren van je sociale media, maar ziet geen commercieel resultaat? De specialist maakt het verschil. Jouw kennis van jouw product en klant, gecombineerd met ons specialisme over sociale media. In zeer diverse branches.</p>
    <p>Wij gebruiken deze kennis voor een contentstrategie op maat. Een strategie die gegarandeerd meer likes, retweets en doorklikken oplevert. Meer likes, meer interactie, meer betrokkenheid: meer omzet.</p>
    <div class="sub">Groeistrategie</div>
    <p>Je netwerk op sociale media laten groeien kan een lastige klus zijn. Maar het levert je enorm veel op. Een groot aantal echte en actieve volgers geeft vertrouwen en genereert nog meer betrokkenheid. Het is de moderne variant van mond-tot-mondreclame.</p>
    <p>Wij hebben de expertise en oplossingen om je al je profielen een echte boost te geven. Met onze tools krijgen we de volledige controle over je kanalen, zodat jij jouw focus kunt richten op de uitvoering en levering van opdrachten.</p>
    <p>En wees voorbereid op groei!</p>
    <h2>Hoe werkt het ?</h2>
    <div class="sub">Quick Scan &amp; advies</div>
    <p>We starten altijd met een grondige analyse van je website en sociale kanalen. Op basis daarvan geven we je een advies over de beste</p>
  </div>
  <div class="page-foot"><span class="foot-url">brindlopq.nl</span><span class="brand-tag">Brindlo</span></div>
</section>

<section class="page" style="left:259px;top:377px;width:193px;height:256px">
  <div class="pad">
    <p><b style="color:var(--navy);font-size:5.6px">Je wilt met ons in zee -</b></p>
    <p>Als je besluit met ons in zee te gaan, doen we dat niet voor een paar weken. Want we doen niet aan 'kil-and-run', maar bouwen aan samenwerking die op de lange termijn echte resultaten oplevert. We moeten elkaar goed leren kennen en dat vraagt tijd.</p>
    <p>Je vertrouwt ons je sociale mediakanalen toe. Dat vraagt vertrouwen en tegelijk moeten wij ons goed inleven in de manier van communicatie die past bij jouw business en jouw doelgroep. Van beide kanten vraagt dit een tijdsinvestering.</p>
    <p><b style="color:var(--navy);font-size:5.6px">Pakketkeuze -</b></p>
    <p>We hebben verschillende servicepakketten waaruit je kunt kiezen wat bij jouw situatie en wensen past. Blijkt op basis van de QuickScan dat je beter af bent met maatwerk, dan maken we daarover specifieke afspraken. Geen twee klanten zijn gelijk, daarom is ons aanbod flexibel opgebouwd.</p>
    <p><b style="color:var(--navy);font-size:5.6px">Implementatie -</b></p>
    <p>Natuurlijk wil je zo snel mogelijk resultaat zien. Dat willen wij ook. We werken de strategie uit in een plan en gaan voor jou aan het werk. Met de prioriteit op die gebieden die zo snel mogelijk resultaten opleveren. Omdat we graag (laten) zien dat onze inspanningen verschil maken. We richten daarvoor de benodigde systemen in. In het begin hebben we regelmatig overleg om elkaar goed te leren kennen en de vinger aan de pols te houden.</p>
    <p><b style="color:var(--navy);font-size:5.6px">Terugkoppeling en verbetering -</b></p>
    <p>Iedere ondernemer is gedreven als het gaat om het behalen van resultaten. Zo ook wij. Wij doen er alles aan om onze dienstverlening zo succesvol mogelijk te laten zijn en jouw sociale doelen te behalen. We hebben regelmatig contact om de resultaten te bespreken en daar waar mogelijk te verbeteren.</p>
  </div>
  <div class="page-foot"><span class="foot-url">brindlopq.nl</span><span class="brand-tag">Brindlo</span></div>
</section>

<section class="page" style="left:478px;top:372px;width:207px;height:261px">
  <div class="pad" style="padding-bottom:0">
    <h2 style="margin-top:0">Wat doen wij</h2>
    <p>Zie onderstaand overzicht onze diensten en services, onder het overzicht beschrijven we de mogelijkheden.</p>
    <table class="services">
      <tr><th></th><th>VL Profiel</th><th>VL Page</th><th>VH Profiel</th><th>VH Groep</th><th>BS Profiel</th><th>BS Page</th><th>PN Page</th><th>VZ Page</th><th>ZB Page</th></tr>
      <tr class="group"><td>On-the-go items</td><td></td><td></td><td></td><td></td><td></td><td></td><td></td><td></td><td></td></tr>
      <tr><td>- Tekst/Foto posts</td><td>✔</td><td>✔</td><td>✔</td><td>✔</td><td>✔</td><td>✔</td><td>✔</td><td>✔</td><td>✔</td></tr>
      <tr><td>- Tekst/Video posts</td><td>✔</td><td>✔</td><td>✔</td><td>✔</td><td>✔</td><td>✔</td><td>✔</td><td>✔</td><td></td></tr>
      <tr class="group"><td>Groei netwerk</td><td></td><td></td><td></td><td></td><td></td><td></td><td></td><td></td><td></td></tr>
      <tr><td>- Volgen/ontvolgen</td><td>✔</td><td></td><td>✔</td><td></td><td>✔</td><td>✔</td><td>✔</td><td></td><td></td></tr>
      <tr><td>- Vrienden/Connecties</td><td>✔</td><td></td><td>✔</td><td>✔</td><td></td><td></td><td></td><td></td><td></td></tr>
      <tr class="group"><td>Interactie</td><td></td><td></td><td></td><td></td><td></td><td></td><td></td><td></td><td></td></tr>
      <tr><td>- Posts likes</td><td>✔</td><td>✔</td><td>✔</td><td>✔</td><td>✔</td><td>✔</td><td>✔</td><td>✔</td><td></td></tr>
      <tr><td>- Comments</td><td>✔</td><td>✔</td><td>✔</td><td>✔</td><td>✔</td><td>✔</td><td>✔</td><td>✔</td><td></td></tr>
      <tr><td>- Berichten</td><td>✔</td><td>✔</td><td>✔</td><td></td><td>✔</td><td>✔</td><td>✔</td><td></td><td></td></tr>
      <tr><td>- Auto antwoord</td><td>✔</td><td>✔</td><td>✔</td><td></td><td>✔</td><td>✔</td><td></td><td></td><td></td></tr>
      <tr class="group"><td>Diversen</td><td></td><td></td><td></td><td></td><td></td><td></td><td></td><td></td><td></td></tr>
      <tr><td>- Datamining</td><td>✔</td><td></td><td>✔</td><td></td><td>✔</td><td></td><td></td><td></td><td></td></tr>
      <tr><td>- Endorse</td><td>✔</td><td></td><td></td><td></td><td></td><td></td><td></td><td></td><td></td></tr>
      <tr><td>- Invite pages</td><td>✔</td><td>✔</td><td>✔</td><td>✔</td><td></td><td></td><td></td><td></td><td></td></tr>
      <tr><td>- Analyse en rapportage</td><td>✔</td><td>✔</td><td>✔</td><td>✔</td><td>✔</td><td>✔</td><td>✔</td><td>✔</td><td>✔</td></tr>
      <tr><td>- Content management</td><td>✔</td><td>✔</td><td>✔</td><td>✔</td><td>✔</td><td>✔</td><td>✔</td><td>✔</td><td>✔</td></tr>
      <tr><td>- SEO</td><td></td><td>✔</td><td></td><td></td><td></td><td>✔</td><td></td><td>✔</td><td>✔</td></tr>
      <tr><td>- SEA</td><td></td><td>✔</td><td></td><td></td><td></td><td>✔</td><td></td><td>✔</td><td>✔</td></tr>
      <tr><td>- Monitoring</td><td>✔</td><td>✔</td><td>✔</td><td>✔</td><td>✔</td><td>✔</td><td>✔</td><td>✔</td><td>✔</td></tr>
    </table>
    <p style="margin-top:6px">*Optioneel bieden wij diensten op Prikwand, Tuimel en Draadnet aan.</p>
  </div>
  <div class="photo" role="img" aria-label="Vervaagde foto van sociale media iconen op een scherm" style="left:0;right:0;bottom:0;height:60px;background:linear-gradient(180deg,rgba(255,255,255,0) 0%,#2a3d66 35%,#15264a 100%)"></div>
  <div class="page-foot dark" style="background:transparent"><span class="foot-url">brindlopq.nl</span><span class="brand-tag">Brindlo</span></div>
</section>

<section class="page" style="left:716px;top:368px;width:201px;height:270px">
  <div class="pad">
    <h2 style="margin-top:0">Geagendeerd posten</h2>
    <p>Geagendeerd posten is meer dan de voorbereiding van posts, het kiezen van de juiste hashtags en het redigeren van teksten. Per platform worden andere formaten van foto's en video's gevraagd. Wij zorgen ervoor dat je voor ieder platform het juiste formaat hebben.</p>
    <p>Daarnaast analyseren wij de posts en doelgroepen zodat we de berichten op het juiste moment van de dag plaatsen, voor het meeste effect en de meeste interactie met de doelgroep.</p>
    <h2>Groei Netwerk</h2>
    <div class="sub">Volgen / ontvolgen</div>
    <p>We zetten onze groeistrategie in op basis van locatie, hashtags, maar ook accounts van concurrenten en activiteit op deze accounts. We volgen relevante profielen, liken een post en wachten een paar dagen. Volgt het profiel ons niet terug, zullen we het ontvolgen en op de blocklist zetten.</p>
    <p>We voorkomen zo dat profielen meerdere keren gevolgd worden. Zo bouwen we aan een nieuw volgersnetwerk dat we verder actief bewerken.</p>
  </div>
  <div class="photo" role="img" aria-label="Foto van iemand achter een laptop in een donkerblauwe omgeving" style="left:0;right:0;bottom:0;height:82px;background:linear-gradient(180deg,#34486f 0%,#1c2f55 55%,#15264a 100%)"></div>
  <div class="page-foot dark" style="background:transparent"><span class="foot-url">brindlopq.nl</span><span class="brand-tag">Brindlo</span></div>
</section>

<section class="page" style="left:957px;top:372px;width:201px;height:266px">
  <div class="photo" role="img" aria-label="Lichte, vervaagde kantoorfoto als kopafbeelding" style="left:0;right:0;top:0;height:60px;background:linear-gradient(180deg,#dfe3ea 0%,#ffffff 100%)"></div>
  <div class="pad" style="position:relative">
    <div class="sub" style="margin-top:0">Vrienden / Connecties</div>
    <p>Voor de groei op Vaklink en Vriendhub gebruiken we een andere strategie, omdat een bedrijfspagina weinig tot geen interactiemogelijkheden biedt. We gebruiken een 'persoonlijk' profiel waarmee we vrienden/connecties maken.</p>
    <p>We gebruiken verschillende criteria zoals lidmaatschap van een groep, werkzaam in bepaalde industrie en dergelijk. Als de vriendschapsverzoeken zijn geaccepteerd, nodigen we deze personen uit om onze bedrijfspagina te volgen.</p>
    <h2>Interactie</h2>
    <div class="sub">Posts / Comments</div>
    <p>We voorzien specifieke content van likes en/of commentaar. Hiervoor stellen we samen specifieke criteria en instellingen op. Zo zorgen we voor zichtbaarheid en interactie met de connecties, vrienden en volgers.</p>
    <h2>Berichten</h2>
    <p>Met behulp van berichten kunnen we volgers, vrienden en connecties benaderen. Niet alleen responsief, maar ook proactief. Zo kunnen we bijvoorbeeld een actie of specifieke content onder de aandacht brengen. In de meeste gevallen kunnen wij deze berichten personaliseren door bijvoorbeeld de voornaam te gebruiken. Het is raadzaam dit spaarzaam in te zetten en zeker niet vaker dan eens per maand. Het doel en de toonzetting moeten passen binnen het netwerk.</p>
  </div>
  <div class="page-foot"><span class="foot-url">brindlopq.nl</span><span class="brand-tag">Brindlo</span></div>
</section>

<!-- Row 3 -->
<section class="page" style="left:41px;top:672px;width:198px;height:264px">
  <div class="pad">
    <div class="sub" style="margin-top:0">Auto antwoord</div>
    <p>Er kunnen verschillende soorten berichten automatisch worden verstuurd. Denk bijvoorbeeld aan een welkomstboodschap als een connectie- of vriendschapsverzoek is geaccepteerd.</p>
    <h2>Diversen</h2>
    <div class="sub">Datamining</div>
    <p>Alle acties die we uitvoeren, leveren data op. Die data verzamelen en registreren we. Op basis van zoekopdrachten kunnen we actief informatie binnenhalen, die we opslaan en op een andere wijze weer kunnen inzetten.</p>
    <p>Als voorbeeld: we kunnen de Vaklink-connectiedata (naam, email, telefoonnummer) binnenhalen en deze in bijvoorbeeld een CRM of mailingsysteem gebruiken.</p>
    <div class="sub">Vaklink interactie</div>
    <p>Iemands vaardigheden op Vaklink bevestigen heeft een waardevol contactmoment. Je kunt specifieke vaardigheden onderschrijven en toont daarmee dat je het profiel hebt bekeken. Het onderschrijven is een cadeautje voor de ontvanger. Vaak wordt er een - al dan niet standaard - bedankje gestuurd.</p>
    <p>Dat bedankje biedt een opening voor een (commerciële) vraag. We kunnen een profiel van een connectie ook alleen 'bekijken', ook hierbij krijgt de connectie een melding. Dit wekt nieuwsgierigheid.</p>
  </div>
  <div class="page-foot"><span class="foot-url">brindlopq.nl</span><span class="brand-tag">Brindlo</span></div>
</section>

<section class="page" style="left:262px;top:672px;width:190px;height:264px">
  <div class="pad navy-fill on-dark" style="padding-bottom:6px">
    <div class="sub" style="margin-top:0">Uitnodigen Pagina's</div>
    <p>Specifiek voor Vriendhub en Vaklink kunnen we de gemaakte vrienden/connecties uitnodigen om de bedrijfspagina te liken/volgen.</p>
  </div>
  <div class="pad">
    <div class="sub" style="margin-top:0">Analyse en rapportage</div>
    <p>Vanuit onze systemen wordt bijgehouden wat de resultaten van de diverse campagnes en acties zijn. Deze analyses gebruiken we om de campagnes verder te optimaliseren en onze klanten te informeren.</p>
    <div class="sub">Content management</div>
    <p>Content en posts kun je zelf maken of voorbereiden, maar wij kunnen dat ook voor je doen. Wij zijn gespecialiseerd in het selecteren van de meest effectieve woorden en hashtags voor jouw doelgroep. Dit is ook een belangrijk onderdeel voor het onderwerp 'zoekmachineoptimalisatie'.</p>
    <p>Wij zorgen in ieder geval voor het agenderen en plaatsen van de posts. Wij bepalen de beste tijden per doelgroep op basis van onze ervaring en analyses. Per platform kunnen we zo de resultaten bijhouden en sturen.</p>
    <div class="sub">Zoekmachineoptimalisatie (SEO)</div>
    <p>Een fantastische marketingkans voor zowel grote als kleine bedrijven en organisaties is hoger in de zoekresultaten te verschijnen.</p>
  </div>
  <div class="page-foot"><span class="foot-url">brindlopq.nl</span><span class="brand-tag">Brindlo</span></div>
</section>

<section class="page" style="left:478px;top:672px;width:207px;height:264px">
  <div class="pad">
    <p>Met een slimme SEO-strategie beïnvloeden we de vindbaarheid van je website in zoekmachines en genereren we onbetaalde traffic naar je website - en daarmee nieuwe leads.</p>
    <p>Dankzij de relatief lage investering en duurzaamheid van de resultaten, zijn wij er vast van overtuigd dat SEO centraal moet staan in je digitale marketingstrategie.</p>
    <div class="sub">SEO voor lokale doelgroepen</div>
    <p>Voor bedrijven met een fysiek bezoekadres is lokaal zoekverkeer ongelooflijk waardevol. Vaak zijn er veel minder middelen en dus investeringen nodig om effectief te scoren op deze zoekwoorden.</p>
    <p>We zijn zeer succesvol in het implementeren van lokale SEO-campagnes met een hoog investeringsrendement. We combineren een uitgebreide analyse van je huidige online aanwezigheid met een grondig zoekwoordonderzoek. Zo optimaliseren we alle beschikbare factoren om de score van je website op de meest waardevolle zoektermen te verhogen.</p>
    <div class="sub">SEO voor lokale doelgroepen</div>
    <p>Adverteren kan natuurlijk altijd. Maar het heeft onze voorkeur – afhankelijk van de fase waarin je sociale media zich bevinden – om organisch op een hoger plan te komen.</p>
    <p>Wil je adverteren, dan kunnen wij dit volledig voor je verzorgen. Van het inregelen van de techniek, het maken van de advertenties, het selecteren van de zoekwoorden en het analyseren en verbeteren van de lopende ads-campagnes.</p>
  </div>
  <div class="page-foot dark"><span class="foot-url">brindlopq.nl</span><span class="brand-tag">Brindlo</span></div>
</section>

<section class="page" style="left:716px;top:672px;width:201px;height:264px">
  <div class="pad">
    <div class="sub" style="margin-top:2px">Monitoring</div>
    <p>Met onze social media monitoringtools meten we zorgvuldig welke acties jouw doelgroep neemt en wat relevant is voor jouw bedrijf. Zo kom je er bijvoorbeeld achter welke opmerkingen je klanten geven over je producten en of er bepaalde klachten zijn.</p>
    <p>Social media monitoring zorgt ervoor dat je hier snel op kunt schakelen en reageren. Interactie met je klanten is offline, maar zeker online heel erg belangrijk!</p>
    <p style="margin-top:10px"><b style="color:var(--navy);font-size:4.8px">Contact details:</b></p>
    <p style="color:var(--muted)">Joris ter Haaksel<br>joris@brindlopq.nl<br>06-47915328</p>
  </div>
  <div class="page-foot"><span class="foot-url">brindlopq.nl</span><span class="brand-tag">Brindlo</span></div>
</section>

<div class="big-brand">
  <div class="ring"></div>
  <div class="name">Brindlo</div>
</div>

</body>
</html>
```